Poetry Book Cover Design Project

Looking for a minimalistic book cover design for a collection of poems. The book title is "Before The Morning Turns To Glass". There are three parts to the book. First covers poetry in the theme of Rage. Second love and desire. The third is strange poems. Essentially the sections are "Rage", "Desire" and the "Strange". The reason for the title "Before The Morning Turns To Glass" is as if someone is writing these till life changes towards the intended outcome as felt in each poem. I want to have the author's name "Nirosha Kulathunge" at the bottom. Ilustration attached.
- Minimalistic

```html
<!DOCTYPE html>
<html lang="en">
<head>
<meta charset="utf-8">
<title>Before The Morning Turns To Glass — Cover</title>
<link rel="stylesheet" href="https://fonts.googleapis.com/css2?family=Roboto+Slab:wght@400;700&display=swap">
<style>
  :root {
    --backdrop: #e3e3e3;
    --paper: #ffffff;
    --ink-blue: #0d4f9c;
    --rule-blue: #5f86c4;
    --disc-warm: #f4a9a4;
    --disc-cool: #2a62ad;
  }
  * { margin: 0; padding: 0; box-sizing: border-box; }
  html, body {
    width: 1200px;
    height: 800px;
    overflow: hidden;
    background: var(--backdrop);
  }
  .canvas {
    position: relative;
    width: 1200px;
    height: 800px;
    display: flex;
    align-items: center;
    justify-content: center;
  }
  .cover {
    position: relative;
    width: 440px;
    height: 680px;
    background: var(--paper);
    box-shadow: 0 6px 24px rgba(0, 0, 0, 0.08);
  }
  .cover-title {
    position: absolute;
    top: 46px;
    right: 34px;
    text-align: right;
    font-family: "Roboto Slab", serif;
    font-weight: 700;
    font-size: 42px;
    line-height: 1.18;
    letter-spacing: -0.5px;
    color: var(--ink-blue);
  }
  .cover-title span { display: block; white-space: nowrap; }
  .cover-art {
    position: absolute;
    top: 262px;
    left: 52px;
    width: 336px;
    height: 336px;
    border-radius: 50%;
    background: linear-gradient(180deg, var(--disc-warm) 0%, var(--disc-cool) 100%);
  }
  .author-block {
    position: absolute;
    bottom: 24px;
    left: 0;
    right: 0;
    text-align: center;
  }
  .author-rule {
    display: block;
    width: 112px;
    height: 1px;
    margin: 0 auto 9px;
    background: var(--rule-blue);
  }
  .author-name {
    font-family: "Roboto Slab", serif;
    font-weight: 400;
    font-size: 15px;
    color: var(--ink-blue);
    letter-spacing: 0.2px;
  }
</style>
</head>
<body>
<main class="canvas">
  <article class="cover">
    <h1 class="cover-title">
      <span>Before The</span>
      <span>Morning Turns</span>
      <span>To Glass</span>
    </h1>

    <div class="cover-art" role="img" aria-label="Round cover artwork: a soft glowing disc fading from warm sunrise tones into deep blue"></div>

    <footer class="author-block">
      <span class="author-rule"></span>
      <p class="author-name">Nirosha Kulathunge</p>
    </footer>
  </article>
</main>
</body>
</html>
```